Keelbrook Vault Holdings Needs A Website

We are looking for a website for a new company. 4 Pages

Needs to be responsive and mobile friendly for all browsers and coded for both Android & IOS. SEO is also important.

Website Brief – Keelbrook Vault Holdings
Domain: www.keelbrookvault.net
Email: info@keelbrookvault.net
Phone: to be inserted later
Address: 40837 52 Ave, Edmonton, AB T6K 3R8
Platform: WordPress (recommended for flexibility, SEO tools, and ease of editing)
Requirements:
• Responsive & mobile-friendly (Android & iOS)
• Cross-browser compatibility
• Fast page load speed
• SEO optimized for storage development, management, and investment keywords
• Easy in-house editing after launch
• Professional, modern, trust-driven design reflecting expertise, reliability, and innovation
________________________________________
Pages
1. HOME
Purpose: Quickly communicate who Keelbrook Vault Holdings is and why they’re the best choice for designing, building, leasing, and managing self storage facilities.
Content Highlights:
• Hero Section: Large, bold image of a modern self storage facility with headline:
"From Concept to Capacity – Your Self Storage Experts"
• Subheadline: “Keelbrook Vault Holdings delivers turnkey design, construction, leasing, and management services for profitable self storage operations.”
• Quick Service Icons:
o Facility Design & Development
o Construction & Build Management
o Lease-Up & Marketing
o Ongoing Facility Management
• Call to Action Button: “LEARN MORE” → links to ABOUT US page.
• Featured Project Highlights: Showcase a few completed or current projects with photos and stats.
• Contact Banner: “Ready to build your next self storage project? Let’s talk.” → CONTACT page.
2. ABOUT US
Purpose: Build credibility, showcase experience, and explain the value proposition.
Content Highlights:
• Who We Are: Overview of Keelbrook Vault Holdings’ history, mission, and team expertise.
• Our Approach: End-to-end process from site selection to occupancy.
• Why Choose Us:
o Industry expertise in self storage
o Proven track record in lease-up success
o Strong vendor and contractor network
3. SERVICES
Purpose: Detail all service offerings with clarity and authority.
Sections:
• Design & Development: Market analysis, site planning, and architectural design.
• Construction Management: Overseeing timelines, budgets, and quality control.
• Lease-Up Strategy: Marketing, promotions, and occupancy acceleration.
• Ongoing Facility Management: Staffing, maintenance, revenue optimization.

4. CONTACT
Purpose: Provide simple, direct ways to connect.
Content Highlights:
• Contact Form (Name, Email, Phone, Message)
• Direct Email: info@keelbrookvault.net
• Phone (if applicable)
• Google Map embed (if there’s a head office location)
• CTA: “Let’s Build Your Storage Success Story.”
Design & Technical Notes
• Visual Style: Clean, modern, bold typography, professional color palette (to be based on branding), strong imagery of self storage facilities.
• Performance: Image compression, caching, responsive scaling.
• SEO Targets: “Self storage facility developer,” “self storage construction,” “self storage management company,” “lease-up services for self storage.”

WordPress or Joomla – must be desktop and mobile friendly with fast page load speed. Need the ability to edit ourselves.

Use pantone colours - #033c5a – dark blue
#2baadf – light blue

```html
<!DOCTYPE html>
<html lang="en">
<head>
<meta charset="utf-8">
<title>Keelbrook Vault Holdings – Self Storage Experts</title>
<link href="https://fonts.googleapis.com/css2?family=Oswald:wght@300;500;600;700&family=Figtree:wght@400;500;600&display=swap" rel="stylesheet">
<style>
:root{
  --navy:#033c5a;
  --navy-deep:#032a42;
  --sky:#2baadf;
  --white:#ffffff;
  --muted:#8fa9bb;
  --line:#1d5576;
}
*{margin:0;padding:0;box-sizing:border-box}
html,body{width:1200px;height:2800px;overflow:hidden}
body{position:relative;background:var(--navy-deep);color:var(--white);font-family:'Figtree',sans-serif}
.abs{position:absolute}
.display{font-family:'Oswald',sans-serif;text-transform:uppercase}
.accent{color:var(--sky)}
.btn{position:absolute;display:flex;align-items:center;justify-content:center;background:var(--sky);color:var(--white);font-family:'Oswald',sans-serif;font-weight:600;font-size:15px;letter-spacing:4px;text-transform:uppercase}

/* header + hero */
.hero{left:0;top:0;width:1200px;height:728px;background:linear-gradient(120deg,#3b5666 0%,#2c4657 45%,#36505f 70%,#263d4c 100%)}
.hero-overlay{left:0;top:0;width:1200px;height:728px;background:rgba(3,42,66,.35)}
.brand{display:flex;align-items:center;gap:10px;font-family:'Figtree',sans-serif;font-weight:600;color:var(--white)}
.brand-mark{width:14px;height:14px;background:var(--sky)}
.site-brand{left:92px;top:34px;font-size:26px}
.nav{top:42px;font-family:'Oswald',sans-serif;font-weight:500;font-size:15px;letter-spacing:3.5px;text-transform:uppercase}
.nav.active{color:var(--sky)}
.follow{left:80px;top:206px;width:24px;height:128px;writing-mode:vertical-rl;transform:rotate(180deg);font-family:'Oswald',sans-serif;font-size:10px;letter-spacing:5px;font-weight:500;text-align:center}
.follow-line{left:92px;top:340px;width:1px;height:110px;background:var(--line)}
.social-dot{left:87px;width:11px;height:11px;border-radius:50%;border:1.5px solid var(--white)}
.hero-title{left:136px;top:206px;font-size:52px;line-height:60px;font-weight:600;letter-spacing:5px}
.hero-sub{left:136px;top:400px;width:530px;font-size:17.5px;line-height:26px}
.slider-ctl{top:316px;font-family:'Oswald',sans-serif;font-size:11px;font-weight:600;letter-spacing:3.5px;display:flex;align-items:center;gap:8px}
.counter{left:1033px;top:608px;font-family:'Oswald',sans-serif;font-weight:600;color:var(--sky);font-size:50px;line-height:60px}
.counter small{font-size:16px;color:var(--muted);letter-spacing:1px;font-weight:500}

/* services */
.services{left:0;top:728px;width:1200px;height:514px;background:var(--navy-deep)}
.service{top:905px;display:flex;align-items:center;gap:14px}
.service-icon{position:relative;width:56px;height:58px}
.service-icon span{position:absolute;right:2px;top:0;width:32px;height:32px;border-radius:50%;background:var(--line)}
.service-icon i{position:absolute;left:4px;top:14px;width:36px;height:40px;border:2px solid var(--sky);border-radius:4px}
.service-name{font-family:'Oswald',sans-serif;font-weight:600;font-size:19px;line-height:25px;letter-spacing:1.6px;text-transform:uppercase}

/* projects */
.projects-head{left:85px;top:1268px;font-size:48px;line-height:62px;font-weight:600;letter-spacing:5px}
.project{top:1348px;width:300px;height:530px}
.p1{left:0;background:linear-gradient(180deg,#8796a3,#5a6670 55%,#c9ccce)}
.p2{left:300px;background:linear-gradient(180deg,#5ba7dc 0%,#a6c8e2 40%,#c29466 75%,#4b7d3a)}
.p3{left:600px;background:linear-gradient(180deg,#f0f0f0,#d7d9d9 50%,#7b8a70)}
.p4{left:900px;background:linear-gradient(180deg,#4a4c5c,#5d4a44 50%,#2b2526)}
.band{left:0;top:1878px;width:1200px;height:22px;background:var(--navy-deep)}

/* cta */
.cta{left:0;top:1900px;width:1200px;height:413px;background:linear-gradient(100deg,#3d4b55,#4e5e68 50%,#3a4952)}
.cta-title{left:0;width:1200px;text-align:center;font-weight:500;letter-spacing:3.5px}

/* footer */
.footer{left:0;top:2313px;width:1200px;height:487px;background:var(--navy-deep)}
.foot-brand{left:86px;top:2436px;font-size:24px}
.foot-social{top:2517px;width:38px;height:38px;border:1px solid var(--line);border-radius:6px;display:flex;align-items:center;justify-content:center}
.foot-social i{width:10px;height:10px;border-radius:50%;background:var(--white)}
.col-head{top:2417px;font-family:'Oswald',sans-serif;font-weight:600;font-size:19px;letter-spacing:3px;color:var(--sky);text-transform:uppercase}
.col-list{list-style:none;top:2462px;font-size:16px;line-height:32px}
.col-list .current{color:var(--sky);font-weight:600}
.hello{left:863px;top:2414px;font-family:'Oswald',sans-serif;font-size:23px;letter-spacing:3px;color:var(--sky)}
.hello b{font-weight:700}
.hello span{font-weight:300}
.addr{left:865px;top:2464px;width:250px;font-size:16px;line-height:20px}
.contact-row{left:865px;display:flex;align-items:center;gap:10px;font-size:16px}
.hex{width:40px;height:40px}
.divider{left:85px;top:2708px;width:1030px;height:1px;background:var(--line)}
.legal{top:2752px;font-family:'Oswald',sans-serif;font-size:12px;letter-spacing:1.2px;color:var(--muted);text-transform:uppercase}
</style>
</head>
<body>

<!-- hero -->
<section class="abs hero" role="img" aria-label="Architectural sketch blended with a modern multi-storey building facade"></section>
<div class="abs hero-overlay"></div>

<header>
  <div class="abs brand site-brand"><span class="brand-mark"></span>Keelbrook Vault Holdings</div>
  <nav>
    <span class="abs nav active" style="left:588px">Home</span>
    <span class="abs nav" style="left:684px">About Us</span>
    <span class="abs nav" style="left:822px">Services</span>
    <span class="btn" style="left:943px;top:27px;width:171px;height:52px">Contact</span>
  </nav>
</header>

<div class="abs follow">Follow Us</div>
<div class="abs follow-line"></div>
<span class="abs social-dot" style="top:467px"></span>
<span class="abs social-dot" style="top:506px"></span>
<span class="abs social-dot" style="top:546px"></span>

<h1 class="abs display hero-title">From concept to<br>capacity–your <span class="accent">self</span><br><span class="accent">storage</span> experts</h1>
<p class="abs hero-sub">Keelbrook Vault Holdings delivers turnkey design, construction, leasing, and management services for profitable self storage operations.</p>
<span class="btn" style="left:137px;top:512px;width:215px;height:52px">Discover More</span>

<div class="abs slider-ctl" style="left:949px;color:var(--muted)">
  <svg width="18" height="8" viewBox="0 0 18 8"><path d="M18 4H2M5 1 2 4l3 3" stroke="currentColor" fill="none" stroke-width="1.3"/></svg>Prew
</div>
<div class="abs slider-ctl" style="left:1049px;color:var(--sky)">Next
  <svg width="18" height="8" viewBox="0 0 18 8"><path d="M0 4h16M13 1l3 3-3 3" stroke="currentColor" fill="none" stroke-width="1.3"/></svg>
</div>
<div class="abs counter">01<small> /03</small></div>

<!-- services -->
<section class="abs services"></section>
<div class="abs service" style="left:85px"><div class="service-icon"><span></span><i></i></div><div class="service-name">Facility design &amp;<br>development</div></div>
<div class="abs service" style="left:367px"><div class="service-icon"><span></span><i></i></div><div class="service-name">Construction &amp;<br>build management</div></div>
<div class="abs service" style="left:661px"><div class="service-icon"><span></span><i></i></div><div class="service-name">Lease-up &amp;<br>marketing</div></div>
<div class="abs service" style="left:884px"><div class="service-icon"><span></span><i></i></div><div class="service-name">Ongoing facility<br>management</div></div>
<span class="btn" style="left:489px;top:1040px;width:197px;height:52px">Learn More</span>

<!-- projects -->
<h2 class="abs display projects-head">Current <span class="accent">Projects</span></h2>
<div class="abs project p1" role="img" aria-label="Curved white modern building with large glass windows"></div>
<div class="abs project p2" role="img" aria-label="White modern house with timber soffit against blue sky"></div>
<div class="abs project p3" role="img" aria-label="Stacked white residence with planted balconies"></div>
<div class="abs project p4" role="img" aria-label="Curved-balcony tower at dusk"></div>
<div class="abs slider-ctl" style="left:85px;top:1608px;color:var(--white)">
  <svg width="18" height="8" viewBox="0 0 18 8"><path d="M18 4H2M5 1 2 4l3 3" stroke="currentColor" fill="none" stroke-width="1.3"/></svg>Prew
</div>
<div class="abs slider-ctl" style="left:1049px;top:1608px;color:var(--sky)">Next
  <svg width="18" height="8" viewBox="0 0 18 8"><path d="M0 4h16M13 1l3 3-3 3" stroke="currentColor" fill="none" stroke-width="1.3"/></svg>
</div>
<div class="abs band"></div>

<!-- contact banner -->
<section class="abs cta" role="img" aria-label="Hand sketching a construction site with tower crane and engineers reviewing plans"></section>
<h2 class="abs display cta-title" style="top:2022px;font-size:44px;line-height:54px">Ready to build your next self storage project?</h2>
<h2 class="abs display cta-title accent" style="top:2080px;font-size:46px;line-height:56px;font-weight:600">Let’s Talk</h2>
<span class="btn" style="left:501px;top:2159px;width:197px;height:51px">Contact Us</span>

<!-- footer -->
<footer class="abs footer"></footer>
<div class="abs brand foot-brand" style="font-size:17px"><span class="brand-mark"></span>Keelbrook Vault Holdings</div>
<span class="abs foot-social" style="left:127px"><i></i></span>
<span class="abs foot-social" style="left:173px"><i></i></span>
<span class="abs foot-social" style="left:219px"><i></i></span>

<h3 class="abs col-head" style="left:373px">Services</h3>
<ul class="abs col-list" style="left:373px">
  <li>Design &amp; Development</li>
  <li>Construction Management</li>
  <li>Lease-Up Strategy</li>
  <li>Ongoing Facility Management</li>
</ul>

<h3 class="abs col-head" style="left:673px">Quick Links</h3>
<ul class="abs col-list" style="left:673px">
  <li class="current">Home</li>
  <li>About Us</li>
  <li>Services</li>
  <li>Contact</li>
</ul>

<h3 class="abs hello"><span>SAYING </span><b>HELLO!</b></h3>
<p class="abs addr">40837 52 Ave, Edmonton, AB T6K 3R8</p>
<div class="abs contact-row" style="top:2524px">
  <svg class="hex" viewBox="0 0 40 40"><path d="M20 1 37 10.5v19L20 39 3 29.5v-19z" fill="var(--sky)"/><rect x="13" y="14" width="14" height="11" rx="1.5" fill="#fff"/><path d="M13 15l7 5 7-5" stroke="var(--sky)" stroke-width="1.5" fill="none"/></svg>
  info@keelbrookvault.net
</div>
<div class="abs contact-row" style="top:2578px">
  <svg class="hex" viewBox="0 0 40 40"><path d="M20 1 37 10.5v19L20 39 3 29.5v-19z" fill="var(--sky)"/><path d="M15 13c-1.5 1-2 3 0 6.5s5 6 7.5 6.5c2 .3 3-.8 3.5-2l-3-2-1.5 1.3c-1.5-.6-3.5-2.6-4-4l1.3-1.5-2-3z" fill="#fff"/></svg>
  1800-555-0192
</div>

<div class="abs divider"></div>
<p class="abs legal" style="left:85px">© 2025 <span class="accent">Keelbrook Vault Holdings</span> &nbsp;All right reserved</p>
<p class="abs legal" style="right:85px">August 18 , 2025. Layout_4</p>

</body>
</html>
```